2 page Web Site Design (Coded), simple, not picky

I need a web portal for a PPC marketing business. I have the logo, some imagery, and some websites to base the design on.

***Background***
The name of the business is "Quiet Harbor Outreach Partners" or QHOP. We provide listings in a searchable database for Dental Sleep Medicine doctors. These are doctors who treat snoring/sleep apnea/and CPAP users with oral appliances. Client doctors will have their own "landing page website" where PPC prospects land from the PPC campaigns. Logos for supporting/landing page websites have been uploaded.
***End Background***

THIS website (for you to design) is to introduce doctors to the concept and detail the services. i.e. PPC campaign management services, listing on a national database of Dental Sleep Medicine practitioners, and a fully featured website dedicated to Snoring, Sleep Apnea, and CPAP Alternative treatment (those websites are "Farewell-Rumble.com", "Farewell-NightPause.com", and ""Farewell-MaskFree.com")

SEM websites whose look I enjoy are:

http://www.brivolta.com/marketing-services/pay-per-click/

http://www.quellandrift.com/welcome/pay-per-click-services/

http://www.tarnolux4co.com/marketing-services/paid-search-management/

The main colors are Red, White, & Blue. Red and blue used mostly for accents/emphasis.

The main/index page's purpose is to, as best possible, convey the idea of SEM campaign management with supporting websites being their best option for internet marketing!
The secondary page is just a slightly modified layout where details can be explained.

Target Market(s)

Dentists who practice Dental Sleep Medicine (see www.pqwrl.org)

Industry/Entity Type

Marketing

Requirements
Must have
• -Sign-up form for the generation of leads... Simple script that sends E-mail is fine... Doctor's Name, Business Name, Business Address, E-mail address, phone #.

-Graphics that will clearly describe the services being provided.

```html
<!DOCTYPE html>
<html lang="en">
<head>
<meta charset="utf-8">
<title>Quiet Harbor Outreach Partners</title>
<link href="https://fonts.googleapis.com/css2?family=Arimo:wght@400;700&family=Questrial&family=Roboto+Condensed:wght@400;700&display=swap" rel="stylesheet">
<style>
:root{
  --red:#b8262e;
  --red-dark:#8f1a20;
  --blue:#1a3a7c;
  --blue-dark:#13306a;
  --navy-text:#1b3f86;
  --ink:#222;
  --body:#3a3a3a;
  --page:#ebebeb;
  --white:#fff;
  --line:#d8d8d8;
  --field:#dcdcdc;
}
*{box-sizing:border-box;margin:0;padding:0}
html,body{width:1063px;height:1200px;overflow:hidden}
body{position:relative;background:var(--page);font-family:Arimo,Arial,sans-serif;color:var(--body)}
.abs{position:absolute}

.header{left:0;top:0;width:1063px;height:80px;background:linear-gradient(#fff,#f4f4f4)}
.nav{left:520px;top:28px;display:flex;align-items:center}
.nav a{font-size:12.5px;color:var(--navy-text);text-decoration:none;position:absolute;top:5px;white-space:nowrap}
.nav .current{left:0;top:0;width:98px;height:23px;border-radius:12px;background:linear-gradient(#3a6fd0,#1a3f98);color:#fff;text-align:center;line-height:23px;border:1px solid #0f2a6a}

.hero-band{left:0;top:80px;width:1063px;height:381px;background:linear-gradient(100deg,#3a4a5a 0%,#6c7a88 25%,#8d7a6c 55%,#5e4438 80%,#3c2b26 100%)}

.logo-card{left:120px;top:0;width:275px;height:138px;background:linear-gradient(#fff,#f0f0f0);border:1px solid #d8d8d8;border-top:none;border-radius:0 0 8px 8px;box-shadow:0 3px 8px rgba(0,0,0,.25);text-align:center}
.logo-name{margin-top:46px;display:flex;align-items:center;justify-content:center;gap:8px;font:700 36px "Roboto Condensed",sans-serif;color:var(--red)}
.logo-name .dot{width:22px;height:22px;border-radius:50%;background:var(--red)}
.logo-sub{font:700 12px "Roboto Condensed",sans-serif;color:var(--red);margin-top:2px}

.hero-panel{left:106px;top:199px;width:531px;height:244px;background:linear-gradient(100deg,rgba(255,255,255,.95),rgba(250,236,238,.85));border:1px solid #fff;border-radius:3px}
.hero-panel h1{position:absolute;left:34px;top:20px;font-weight:400;color:var(--navy-text);line-height:31px}
.hero-panel h1 .thin{display:block;font:400 26px Questrial,sans-serif}
.hero-panel h1 .bold{display:block;font:700 24.5px Arimo,sans-serif}
.hero-art{left:31px;top:85px;width:129px;height:151px;border-radius:40% 40% 30% 30%;background:linear-gradient(#f7e7e9,#e0a8b0)}
.hero-list{position:absolute;left:170px;top:102px;width:355px;list-style:none;font-size:12.5px;line-height:15px;color:var(--ink)}
.hero-list li{position:relative;padding-left:20px;margin-bottom:25px}
.hero-list li::before{content:"";position:absolute;left:6px;top:4px;border-left:7px solid transparent;border-top:7px solid var(--red)}

.card{color:#fff;border-radius:3px}
.card h2{font:400 21px "Roboto Condensed",sans-serif;text-align:center}
.card .sub{font-size:12px;text-align:center;margin-top:2px}
.card .rule{height:1px;margin:13px 0 0;background:rgba(255,255,255,.2)}
.card ul{list-style:none;font-size:11px;line-height:13px}
.card li{position:relative;padding-left:28px}
.card li::before{content:"";position:absolute;left:14px;top:3px;border-top:3px solid transparent;border-bottom:3px solid transparent;border-left:4px solid #fff}

.sem-card{left:657px;top:184px;width:275px;height:313px;background:linear-gradient(var(--red),#a81f27);border:2px solid #e1e1e1;padding-top:14px}
.sem-card p{font-size:11px;line-height:13px;padding:14px 14px 0 13px}
.sem-card ul{margin-top:13px;padding-right:12px}
.sem-card li{margin-bottom:11px}
.btn-more{position:absolute;left:170px;top:274px;width:88px;height:22px;border-radius:11px;background:linear-gradient(#3a6fd0,#1a3f98);border:1px solid #0f2a6a;color:#fff;font-size:12.5px;text-align:center;line-height:20px}
.shadow{height:10px;border-radius:50%;background:radial-gradient(ellipse,rgba(0,0,0,.18),transparent 70%)}

.content{left:106px;top:484px;width:850px;height:661px;background:var(--white);border:1px solid #dcdcdc;border-radius:3px}
.main{position:absolute;left:22px;top:42px;width:513px}
.main h2{font:400 21px "Roboto Condensed",sans-serif;color:var(--ink);padding-bottom:9px;border-bottom:1px solid var(--line);margin-left:1px}
.main p{font-size:11px;line-height:16px;color:#444}
.main h3{font:700 15px "Roboto Condensed",Arial,sans-serif;letter-spacing:.2px}
.intro{margin-top:10px}
.h-red{color:var(--red);margin-top:17px}
.h-blue{color:var(--navy-text);margin-top:24px}
.main .lead{margin-top:16px}
.shots{display:flex;justify-content:space-between;margin-top:16px}
.shot{width:251px;height:228px;border:1px solid #ccc;padding:3px;background:#fff}
.shot div{width:100%;height:100%;background:linear-gradient(#f6f3e6,#e9edf7)}
.ppc-list{list-style:none;margin-top:12px;font-size:11px;line-height:16px;color:#444}
.ppc-list li{position:relative;padding-left:12px}
.ppc-list li::before{content:"";position:absolute;left:1px;top:5px;border-top:3px solid transparent;border-bottom:3px solid transparent;border-left:4px solid var(--red)}
.read-more{display:block;margin-top:2px;font-size:10px;font-weight:700;color:var(--navy-text);text-decoration:none}

.ppc-card{left:659px;top:531px;width:274px;height:259px;background:linear-gradient(var(--blue),var(--blue-dark));padding-top:13px}
.ppc-card ul{margin-top:13px;padding-right:14px}
.ppc-card li{margin-bottom:10px}

.signup{left:659px;top:813px;width:274px;height:286px;background:#fff;border:1px solid #dcdcdc;border-radius:3px}
.signup h2{font:400 21px "Roboto Condensed",sans-serif;color:var(--ink);text-align:center;padding:13px 0 12px;border-bottom:1px solid #e2e2e2;background:linear-gradient(#fff,#f6f6f6)}
.field{position:absolute;left:18px;font-size:11px;color:#333}
.field label{position:absolute;left:0;top:2px;white-space:nowrap}
.field input,.field textarea{position:absolute;left:107px;width:134px;height:19px;border:1px solid #bbb;border-radius:3px;background:linear-gradient(#c9c9c9,#ececec);font:inherit}
.field textarea{height:57px;resize:none}
.submit{position:absolute;left:125px;top:248px;width:81px;height:23px;border-radius:12px;border:1px solid #6e1216;background:linear-gradient(#c8323a,#8f1a20);color:#fff;font:12.5px Arimo,sans-serif}

.footer{left:108px;top:1160px;font-size:9px;line-height:11px;color:#555}
</style>
</head>
<body>
<header class="abs header">
  <nav class="abs nav">
    <a class="current" href="#">Landing Page</a>
    <a href="#" style="left:164px">About</a>
    <a href="#" style="left:273px">Services</a>
    <a href="#" style="left:380px">Contact</a>
  </nav>
</header>

<div class="abs hero-band" role="img" aria-label="Blurred photograph of a dentist at work in a practice"></div>

<div class="abs logo-card">
  <div class="logo-name"><span class="dot"></span>QHOP LLC</div>
  <div class="logo-sub">Quiet Harbor Outreach Partners</div>
</div>

<section class="abs hero-panel">
  <h1><span class="thin">Customized internet marketing solution</span><span class="bold">specially designed for OSB Therapists!</span></h1>
  <div class="abs hero-art" role="img" aria-label="Illustration of a tooth cross-section"></div>
  <ul class="hero-list">
    <li>Will drive customers to your practice with PPC Search engine Marketing and then educate them about the unique benefits inherent to OAT therapy with a dedicated website .</li>
    <li>Each participant has a customized “landing page” on are a website that exclusively promotes the OSB therapies and OSB therapists.</li>
  </ul>
</section>

<section class="abs card sem-card">
  <h2>Search Engine Marketing</h2>
  <div class="sub">Online marketing strategy</div>
  <div class="rule"></div>
  <p>Search engine marketing is an online marketing strategy that aims to increase qualified visitor traffic to your website by positioning your advertisements at the top and right side of “natural” and “organic” search result pages</p>
  <ul>
    <li>You only pay when someone clicks on one of your advertisements.</li>
    <li>It is estimated that pay per click ads receive around 30% of all clicks on search engines.</li>
    <li>Findwell Adwords, Yonder Search Marketing and Marlow Adcenter are pay per click advertising platforms.</li>
  </ul>
  <a class="btn-more" href="#">More</a>
</section>
<div class="abs shadow" style="left:680px;top:500px;width:230px"></div>

<main class="abs content">
  <div class="main">
    <h2>Welcome to Quiet Harbor Outreach Partners</h2>
    <p class="intro">will drive customers to your practice with PPC Search engine Marketing and then educate them about the unique benefits inherent to OAT therapy with a dedicated website .</p>
    <h3 class="h-red">What is Search Engine Marketing?</h3>
    <p class="lead">Search engine marketing is an online marketing strategy that aims to increase qualified visitor traffic to your website by positioning your advertisements at the top and right side of “natural” and “organic” search result pages [descriptions below].</p>
    <div class="shots">
      <div class="shot"><div role="img" aria-label="Search results page with paid pay per click listings highlighted"></div></div>
      <div class="shot"><div role="img" aria-label="Search results page with natural search results highlighted"></div></div>
    </div>
    <h3 class="h-blue">Search Engine Marketing(Pay Per Click)</h3>
    <p class="lead">Paid search results, called “Pay Per Click” (PPC) advertising, promote websites in “Sponsored” section of search results.</p>
    <ul class="ppc-list">
      <li>You only pay when someone clicks on one of your advertisements.</li>
      <li>It is estimated that pay per click ads receive around 30% of all clicks on search engines.</li>
      <li>Findwell Adwords, Yonder Search Marketing and Marlow Adcenter are pay per click advertising platforms.</li>
    </ul>
    <a class="read-more" href="#">Read More...</a>
  </div>
</main>

<section class="abs card ppc-card">
  <h2>Pay Per Click</h2>
  <div class="sub">Search Engine Marketing Campaign Managment.</div>
  <div class="rule"></div>
  <ul>
    <li>We set up and manage your search engine marketing campaigns for you.</li>
    <li>You only pay when visitors click on your ad and visit your website.</li>
    <li>We design your ad campaign to optimize ad click conversion rates.</li>
    <li>We send you regular advertising effectiveness monitoring, and analysis reports so you can determine your return-on-investment and adjust your budget accordingly.</li>
  </ul>
</section>

<form class="abs signup">
  <h2>Signup Today!</h2>
  <div class="field" style="top:67px"><label>Doctor's Name</label><input type="text"></div>
  <div class="field" style="top:94px"><label>Business Name</label><input type="text"></div>
  <div class="field" style="top:121px"><label>Business Address</label><textarea></textarea></div>
  <div class="field" style="top:185px"><label style="left:3px">E-mail address</label><input type="email"></div>
  <div class="field" style="top:212px"><label>Phone.No</label><input type="tel"></div>
  <button class="submit" type="submit">Submit</button>
</form>
<div class="abs shadow" style="left:685px;top:1096px;width:225px"></div>

<footer class="abs footer">Copyrights@Quiet Harbor Outreach Partners.com<br>All rights reserved.</footer>
</body>
</html>
```